Professional BIO Template with photo and logo

Hello,
I need a professional Bio template developed via Microsoft WORD ASAP!!!!! I would like to just be able to add the text I need to add. So resize-able text boxes. Potentially able to adjust the font. These are the things I need added it to include.
Head shot (attached)
Text Box for Name
Text Box for phone number
Text box for email
KTW Logo (attached)
Maybe a blue banner at the top or some background boxes that are blue or grey. Here are the pantone colors that our company uses.

CORE COLOR
100c 91m 17y 6k 38r 58g 128b Hex #263A80 Pantone 7687 C

CORE CONTRAST COLOR
36c 29m 28y 0k 168r 168g 170b Hex #669999 Pantone Cool Gray 6C

I also attached some examples of what we have been looking at. Instead of green add the blue...instead of black maybe just be white.

Thank you

```html
<!DOCTYPE html>
<html lang="en">
<head>
<meta charset="utf-8">
<title>Evan Marlow – Bio</title>
<link rel="stylesheet" href="https://fonts.googleapis.com/css2?family=EB+Garamond:wght@700&family=Outfit:wght@300;400;700;800&display=swap">
<style>
  :root {
    --core-blue: #263a80;
    --deep-navy: #1e2a63;
    --contrast-gray: #a7a9ac;
    --contrast-teal: #669999;
    --deep-teal: #2d6363;
    --soft-teal: #dce8e8;
    --ink: #3a3a3a;
    --title-gray: #6d6e71;
    --backdrop: #5f5f5f;
    --paper: #ffffff;
  }
  * { box-sizing: border-box; margin: 0; padding: 0; }
  html, body { width: 1095px; height: 1200px; overflow: hidden; background: var(--backdrop); }
  .bio-page {
    position: absolute; left: 202px; top: 85px;
    width: 739px; height: 1045px;
    background: var(--paper);
    font-family: "Outfit", sans-serif;
    overflow: hidden;
  }
  .page-shapes { position: absolute; inset: 0; }
  .headshot {
    position: absolute; left: 27px; top: 86px; width: 209px; height: 215px;
    background: var(--paper); padding: 6px;
  }
  .headshot-fill {
    width: 100%; height: 100%;
    background: radial-gradient(circle at 50% 40%, #8a7466 0%, #5a5654 35%, #2f3033 75%, #1e2026 100%);
  }
  .person-name {
    position: absolute; left: 295px; top: 26px;
    font-family: "EB Garamond", serif; font-weight: 700;
    font-size: 74px; line-height: 1; color: var(--core-blue); letter-spacing: -0.5px;
  }
  .name-rule { position: absolute; left: 295px; top: 98px; width: 406px; height: 3px; background: var(--title-gray); }
  .person-title {
    position: absolute; left: 298px; top: 106px;
    font-weight: 800; font-size: 12px; letter-spacing: 1.6px; color: var(--title-gray);
  }
  .bio-text {
    position: absolute; left: 332px; top: 184px; width: 393px;
    font-weight: 300; font-size: 11.8px; line-height: 14.9px; color: var(--ink);
  }
  .bio-text p { padding: 0 10px; margin-top: 14.9px; }
  .bio-text .bio-lead { background: var(--soft-teal); padding: 8px 10px 7px; margin-top: 0; }
  .bio-text .bio-after-lead { margin-top: 8px; }
  .bio-text .ln { display: block; white-space: nowrap; text-align: justify; text-align-last: justify; }
  .contact { position: absolute; color: #fff; font-size: 13px; line-height: 16.5px; font-style: normal; }
  .contact-address { right: 536px; top: 354px; text-align: right; font-weight: 300; }
  .contact-phone { right: 526px; top: 429px; text-align: right; font-weight: 700; }
  .contact-email { left: 66px; top: 499px; font-weight: 300; }
  .contact strong { font-weight: 700; }
  .brand-mark {
    position: absolute; left: 62px; top: 860px; width: 222px;
    display: flex; align-items: center; justify-content: center; gap: 14px;
    color: #fff; font-weight: 700; font-size: 66px; letter-spacing: 4px; line-height: 1;
  }
  .brand-mark .brand-square { width: 20px; height: 20px; background: #fff; }
  .site-url {
    position: absolute; left: 327px; top: 998px; width: 412px; height: 47px;
    display: flex; align-items: center; justify-content: center;
    font-family: "EB Garamond", serif; font-weight: 700; font-size: 14px;
    letter-spacing: 4.5px; color: #1b1b2a;
  }
</style>
</head>
<body>
<main class="bio-page">
  <svg class="page-shapes" width="739" height="1045" viewBox="0 0 739 1045" aria-hidden="true">
    <polygon class="side-panel" points="0,0 258,0 327,1045 0,1045" fill="var(--core-blue)"/>
    <polygon class="header-band" points="267,129 739,129 739,167 269,167" fill="var(--contrast-gray)"/>
    <rect class="footer-band" x="327" y="998" width="412" height="47" fill="var(--contrast-teal)"/>
    <rect class="side-rule" x="29" y="339" width="2.5" height="678" fill="var(--contrast-gray)"/>
    <polygon points="213,357 296,371 299,408 215,404" fill="var(--deep-navy)"/>
    <polygon points="285,407 299,408 284,421" fill="#141c47"/>
    <path d="M257,373 a9,9 0 0 1 9,9 c0,7 -9,16 -9,16 c0,0 -9,-9 -9,-16 a9,9 0 0 1 9,-9z" fill="#fff"/>
    <circle cx="257" cy="382" r="3.3" fill="var(--deep-navy)"/>
    <polygon points="218,423 302,439 304,476 220,470" fill="var(--deep-teal)"/>
    <polygon points="290,474 304,476 289,489" fill="#1d4545"/>
    <path d="M254,444 l5,0 2,7 -3,2 c1,3 1,5 0,8 l3,2 -2,7 -5,0 c-4,-7 -4,-19 0,-26z" fill="#fff"/>
    <path d="M265,451 a5,6 0 0 1 0,10 M269,447 a9,10 0 0 1 0,18" fill="none" stroke="#fff" stroke-width="2" stroke-linecap="round"/>
    <polygon points="224,487 307,502 308,541 225,535" fill="var(--contrast-gray)"/>
    <polygon points="295,539 308,541 294,552" fill="#7e8084"/>
    <text x="261" y="526" text-anchor="middle" font-family="Outfit, sans-serif" font-weight="800" font-size="29" fill="#fff">@</text>
  </svg>

  <div class="headshot"><div class="headshot-fill" role="img" aria-label="Headshot portrait of Evan Marlow"></div></div>

  <h1 class="person-name">Evan Marlow</h1>
  <div class="name-rule"></div>
  <p class="person-title">CHIEF OPERATIONS OFFICER, KTW INC.</p>

  <address class="contact contact-address">218 Ridgeview Lane<br>Suite 200<br><strong>Larkspur, CO 80555</strong></address>
  <p class="contact contact-phone">Phone: 555-014-2283<br>Fax: 555-014-7710</p>
  <p class="contact contact-email">Evanmarlow@mail.com</p>

  <div class="brand-mark"><span>KTW</span><span class="brand-square"></span></div>

  <section class="bio-text">
    <p class="bio-lead"><span class="ln">Lorem Ipsum is simply dummy text of the printing and typesetting</span><span class="ln">industry. Lorem Ipsum has been the industry's standard dummy</span><span class="ln">text ever since the 1500s, when an unknown printer took a galley</span><span class="ln">of type and scrambled it to make a type specimen book. It has</span><span class="ln">survived not only five centuries, but also the leap into electronic</span><span class="ln">typesetting, remaining essentially unchanged. It was popularised</span><span class="ln">in the 1960s with the release of Letraset sheets containing Lorem</span><span class="ln">Ipsum passages, and more recently with desktop publishing</span><span class="ln">software like Aldus PageMaker including versions of Lorem Ipsum.</span></p>
    <p class="bio-after-lead"><span class="ln">Lorem Ipsum is simply dummy text of the printing and typesetting</span><span class="ln">industry. Lorem Ipsum has been the industry's standard dummy</span><span class="ln">text ever since the 1500s, when an unknown printer took a galley</span><span class="ln">of type and scrambled it to make a type specimen book. It has</span><span class="ln">survived not only five centuries, but also the leap into electronic</span><span class="ln">typesetting, remaining essentially unchanged. It was popularised</span><span class="ln">in the 1960s with the release of Letraset sheets containing Lorem</span><span class="ln">Ipsum passages, and more recently with desktop publishing</span><span class="ln">software like Aldus PageMaker including versions of Lorem Ipsum.</span></p>
    <p><span class="ln">Lorem Ipsum is simply dummy text of the printing and typesetting</span><span class="ln">industry. Lorem Ipsum has been the industry's standard dummy</span><span class="ln">text ever since the 1500s, when an unknown printer took a galley</span><span class="ln">of type and scrambled it to make a type specimen book. It has</span><span class="ln">survived not only five centuries, but also the leap into electronic</span><span class="ln">typesetting, remaining essentially unchanged. It was popularised</span><span class="ln">in the 1960s with the release of Letraset sheets containing Lorem</span><span class="ln">Ipsum passages, and more recently with desktop publishing</span><span class="ln">software like Aldus PageMaker including versions of Lorem Ipsum.</span></p>
    <p><span class="ln">Lorem Ipsum is simply dummy text of the printing and typesetting</span><span class="ln">industry. Lorem Ipsum has been the industry's standard dummy</span><span class="ln">text ever since the 1500s, when an unknown printer took a galley</span><span class="ln">of type and scrambled it to make a type specimen book. It has</span><span class="ln">survived not only five centuries, but also the leap into electronic</span><span class="ln">typesetting, remaining essentially unchanged. It was popularised</span><span class="ln">in the 1960s with the release of Letraset sheets containing Lorem</span><span class="ln">Ipsum passages, and more recently with desktop publishing</span><span class="ln">software like Aldus PageMaker including versions of Lorem Ipsum.</span></p>
    <p><span class="ln">Lorem Ipsum is simply dummy text of the printing and typesetting</span><span class="ln">industry. Lorem Ipsum has been the industry's standard dummy</span><span class="ln">text ever since the 1500s, when an unknown printer took a galley</span><span class="ln">of type and scrambled it to make a type specimen book. It has</span><span class="ln">survived not only five centuries, but also the leap into electronic</span><span class="ln">typesetting, remaining essentially unchanged. It was popularised</span><span class="ln">in the 1960s with the release of Letraset sheets containing Lorem</span><span class="ln">Ipsum passages, and more recently with desktop publishing</span><span class="ln">software like Aldus PageMaker including versions of Lorem Ipsum.</span></p>
    <p><span class="ln">Lorem Ipsum is simply dummy text of the printing and typesetting</span><span class="ln">industry. Lorem Ipsum has been the industry's standard dummy</span></p>
  </section>

  <div class="site-url">WWW.KTWINC.COM</div>
</main>
</body>
</html>
```